VLM8 Business Card Design Project

Design which catches the client with the first impression. A design which is professional and classy with elegance. We have also got another project running and the winning prize for that is $240 "vlm8 print + graphic design".
For all the company details please visit www.vlm8-example.com.
Please find the logo attached and i would like to have good colors for my business card.
, Design which catches the client with the first impression. A design which is professional and classy with elegance.
Updates
VLM8 is running two projects at the same time, please feel free to participate. The other project name is

```html
<!DOCTYPE html>
<html lang="en">
<head>
<meta charset="utf-8">
<title>VLM8 Business Card</title>
<link rel="stylesheet" href="https://fonts.googleapis.com/css2?family=Open+Sans:wght@400;600;700;800&display=swap">
<style>
  :root {
    --backdrop: #e4e4e2;
    --card-dark: #3a3a3c;
    --card-back: #333335;
    --card-white: #ffffff;
    --brand-green: #3dba8c;
    --brand-lime: #8cc63f;
    --ink: #141414;
    --light-text: #f2f2f2;
  }
  * { margin: 0; padding: 0; box-sizing: border-box; }
  html, body { width: 1200px; height: 900px; overflow: hidden; }
  body {
    background: var(--backdrop);
    font-family: "Open Sans", Arial, sans-serif;
    position: relative;
  }
  .card {
    position: absolute;
    left: 285px;
    width: 630px;
    height: 360px;
    overflow: hidden;
    box-shadow: 0 10px 30px rgba(0,0,0,0.18);
  }
  /* Back of card */
  .card-back {
    top: 60px;
    background: var(--card-back);
    display: flex;
    align-items: center;
    justify-content: center;
  }
  .back-lockup {
    display: flex;
    flex-direction: column;
    align-items: flex-start;
  }
  .back-name-row {
    display: flex;
    align-items: center;
    gap: 16px;
  }
  .back-dot {
    width: 44px; height: 44px;
    border-radius: 50%;
    background: var(--light-text);
  }
  .back-name {
    font-size: 82px;
    font-weight: 600;
    color: var(--light-text);
    line-height: 1;
    letter-spacing: 1px;
  }
  .back-url {
    margin-top: 8px;
    margin-left: 60px;
    font-size: 30px;
    font-weight: 700;
    color: var(--brand-lime);
    line-height: 1;
  }
  /* Front of card */
  .card-front {
    top: 480px;
    background: var(--card-white);
  }
  .name-strip {
    position: absolute;
    left: 0; top: 0; right: 0;
    height: 64px;
    padding: 10px 0 0 330px;
  }
  .holder-name {
    font-size: 28px;
    font-weight: 800;
    color: var(--ink);
    line-height: 1;
  }
  .holder-position {
    margin-top: 4px;
    font-size: 12px;
    color: var(--brand-green);
  }
  .dark-panel {
    position: absolute;
    left: 0; right: 0;
    top: 64px;
    height: 226px;
    background: var(--card-dark);
  }
  .contact {
    position: absolute;
    left: 360px;
    top: 96px;
    color: var(--light-text);
    font-size: 14px;
    line-height: 1.4;
  }
  .contact-label {
    color: var(--brand-green);
    font-size: 13px;
    letter-spacing: 0.5px;
    display: flex;
    align-items: center;
    gap: 6px;
  }
  .contact-label svg { width: 12px; height: 12px; fill: var(--brand-green); }
  .contact-lines { padding-left: 18px; margin-bottom: 8px; }
  .brand-wordmark {
    position: absolute;
    left: 30px;
    bottom: 8px;
    display: flex;
    align-items: flex-end;
    gap: 14px;
  }
  .brand-dot {
    width: 40px; height: 40px;
    border-radius: 50%;
    background: var(--brand-lime);
    margin-bottom: 128px;
  }
  .brand-name {
    font-size: 170px;
    font-weight: 700;
    color: var(--brand-green);
    line-height: 0.8;
    letter-spacing: -2px;
  }
</style>
</head>
<body>
  <section class="card card-back" aria-label="Card back">
    <div class="back-lockup">
      <div class="back-name-row">
        <span class="back-dot"></span>
        <span class="back-name">VLM8</span>
      </div>
      <span class="back-url">vlm8-example.com</span>
    </div>
  </section>

  <section class="card card-front" aria-label="Card front">
    <div class="name-strip">
      <div class="holder-name">Your Name</div>
      <div class="holder-position">Company Position</div>
    </div>
    <div class="dark-panel"></div>
    <div class="contact">
      <div class="contact-label">
        <svg viewBox="0 0 12 12" aria-hidden="true"><path d="M6 0 0 5.5h1.8V12h3V8h2.4v4h3V5.5H12z"/></svg>
        ADDRESS
      </div>
      <div class="contact-lines">
        1750 Your Address<br>Suite 1500<br>City, ST 22102
      </div>
      <div class="contact-label">
        <svg viewBox="0 0 12 12" aria-hidden="true"><path d="M2.5 0 4.5 2.8 3.3 4.2c.8 1.8 2.3 3.3 4.5 4.5l1.4-1.2L12 9.5 10.5 12C5 11.4.6 7 0 1.5z"/></svg>
        PHONE NUMBER
      </div>
      <div class="contact-lines">000 123 4567</div>
    </div>
    <div class="brand-wordmark">
      <span class="brand-dot"></span>
      <span class="brand-name">VLM8</span>
    </div>
  </section>
</body>
</html>
```